Tolvek Consulting
Tolvek Consulting stationary
Tolvek Consulting - Consulting
Creative Brief
Professional
Daniel R. Tolvek
Chief Executive Officer
Tolvek Consulting, LLC P.O. Box 4372 Phoenix, AZ 85004
daniel@danielrtolvek-mail.com
danielrtolvek-mail.com
Tolvek Consulting Logo

```html
<!DOCTYPE html>
<html lang="en">
<head>
<meta charset="utf-8">
<title>Tolvek Consulting – Business Card</title>
<link rel="stylesheet" href="https://fonts.googleapis.com/css2?family=Source+Sans+3:wght@400;600;700&display=swap">
<style>
  :root {
    --backdrop: #e9e6e2;
    --card-white: #ffffff;
    --brand-blue: #1f57a8;
    --brand-orange: #f47a1f;
    --band-navy: #0b1d5a;
    --band-cyan: #1cc5d8;
    --text-light: #ffffff;
  }
  * { margin: 0; padding: 0; box-sizing: border-box; }
  html, body {
    width: 1200px; height: 965px; overflow: hidden;
    background: var(--backdrop);
    font-family: "Source Sans 3", "Helvetica Neue", Arial, sans-serif;
  }
  .canvas { position: relative; width: 1200px; height: 965px; }
  .business-card {
    position: absolute; left: 80px; top: 184px;
    width: 1040px; height: 597px;
    border-radius: 42px; overflow: hidden;
    background: var(--card-white);
    box-shadow: 0 6px 18px rgba(0,0,0,0.18);
  }
  .card-bands { position: absolute; inset: 0; width: 100%; height: 100%; }
  .brand-lockup {
    position: absolute; left: 0; right: 0; top: 120px;
    display: flex; justify-content: center; align-items: center; gap: 22px;
  }
  .brand-mark { width: 46px; height: 46px; background: var(--brand-orange); }
  .brand-name {
    font-size: 64px; font-weight: 700; color: var(--brand-blue);
    letter-spacing: 1px; line-height: 1;
  }
  .holder {
    position: absolute; right: 600px; top: 420px;
    text-align: right; color: var(--text-light);
  }
  .holder-name { font-size: 35px; font-weight: 700; line-height: 1.15; }
  .holder-title { font-size: 27px; font-weight: 400; line-height: 1.2; }
  .divider {
    position: absolute; left: 453px; top: 368px;
    width: 2px; height: 208px; background: var(--text-light);
  }
  .contact {
    position: absolute; left: 485px; top: 368px;
    color: var(--text-light); font-size: 27px; line-height: 36px;
  }
  .contact .company { margin-bottom: 0; }
  .contact .gap { height: 28px; }
  .contact b { font-weight: 700; }
</style>
</head>
<body>
<div class="canvas">
  <div class="business-card">
    <svg class="card-bands" viewBox="0 0 1040 597" preserveAspectRatio="none" aria-hidden="true">
      <defs>
        <linearGradient id="bandGradient" x1="0" y1="0" x2="1" y2="0">
          <stop offset="0" stop-color="var(--band-navy)" style="stop-color:#0b1d5a"/>
          <stop offset="0.45" stop-color="#0e3f86"/>
          <stop offset="1" stop-color="#1cc5d8"/>
        </linearGradient>
      </defs>
      <path d="M0,278 C300,248 640,288 1040,342 L1040,362 C620,306 280,282 0,328 Z" fill="#f47a1f"/>
      <path d="M0,328 C280,282 620,306 1040,362 L1040,597 L0,597 Z" fill="url(#bandGradient)"/>
    </svg>

    <div class="brand-lockup">
      <span class="brand-mark"></span>
      <span class="brand-name">Tolvek Consulting</span>
    </div>

    <div class="holder">
      <p class="holder-name">Daniel R. Tolvek</p>
      <p class="holder-title">Chief Executive Officer</p>
    </div>

    <div class="divider"></div>

    <div class="contact">
      <p class="company">Tolvek Consulting, LLC</p>
      <p>P.O. Box 4372, Phoenix, AZ 85004</p>
      <div class="gap"></div>
      <p><b>M :</b> 480.555.0142</p>
      <p><b>E :</b> daniel@danielrtolvek-mail.com</p>
      <p><b>W :</b> www.danielrtolvek-mail.com</p>
    </div>
  </div>
</div>
</body>
</html>
```